Bus Card for Organic Hydroponic Produce company

We need a business card for a budding new business. We grow 100% organic, 100% hydroponic, 100% GMO free produce for sale in our local area. We need something bold and dynamic, not simple and elegant. We want to catch peoples attention and get them to visit our website to view more information about our products and services. Its difficult to explain on a business card the differences between our produce (tomatoes, cucumbers, peppers, etc...) and the kind they would buy at the local grocer or market. , so we need to push them to the website.
We have been brainstorming names for the company and have a few in mind, so choose whichever speaks most to your artistic flair and propose a card based on that one, or both. #1 "Marrowfield Organics" with a slogan something like....." When merely growing green merely isn't quite enough" OR #2 "Quillbrook Organics" with a slogan similar to...."The cutting edge in cleaner, purer organics" OR #3" "Tandrel Organics" with a slogan similar to: "Building a healthier future for those we leave behind"" OR #4 "Loamwise Path" with a slogan similar to: "Purity by Simplicity"
Eventually we will need assistance with web design, promotional and sales materials, etc. so if you offer those services, please indicate that with the design, though it is NOT necessary to offer any additional services to win this contest. WE will pick the winner solely on the business card we like the most.
We want something that stands out, and especially with the name "Oda's organics", we understand that a creative mind may wander into certain attention getting means that may not be quite within the realm of what we can hand out at our local grocer or farmers market. We definitely are not opposed to a little salacious undertone or allusion to attract attention, but please keep it tasteful if you skirt that grey area.
For our card, we use an online printer that can add foils, special die cuts, double sided cards, 3-d cards (we love these 32 pt cards), transparent or translucent cards and more. We love cards that have some of these things where possible and on all of our other business' cards we get rave reviews from customers about their uniqueness. plumtessa.com has the info on these accents if you wish to view what I am referencing.
So in conclusion, we want a unique, stylish, bold, vivid, 2 sided business card that will really stand out. Just usw a generic phone number and website for now and we will add them as they become available. Please email with any questions! Thanks in advance for your effort and creativity!
Target Market(s)
We are targeting parents who are conceintous of what their children and families are eating. Our target audience are moms, but we don't want to exclude anyone else who chooses to eat more healthy. Our target customer is the same customer that would shop at Brightcart stores or local farmers markets

```html
<!DOCTYPE html>
<html lang="en">
<head>
<meta charset="utf-8">
<title>Fernhollow Greens — Business Card</title>
<link href="https://fonts.googleapis.com/css2?family=Questrial&display=swap" rel="stylesheet">
<style>
  :root {
    --stage: #ecebe6;
    --ink-black: #0a0a0a;
    --leaf: #8cc63f;
    --leaf-deep: #1f7a34;
    --paper: #ffffff;
    --text-light: #f2f2f2;
    --slogan: #2f5b1f;
  }
  html, body {
    margin: 0;
    width: 1200px;
    height: 1000px;
    overflow: hidden;
    background: var(--stage);
    font-family: "Questrial", "Century Gothic", sans-serif;
  }
  .sheet {
    position: relative;
    width: 1200px;
    height: 1000px;
  }
  .card {
    position: absolute;
    left: 250px;
    width: 700px;
    height: 400px;
    border-radius: 46px;
    overflow: hidden;
    box-shadow: 0 6px 18px rgba(0,0,0,0.18);
  }
  .card--back { top: 70px; background: var(--ink-black); }
  .card--front { top: 530px; background: var(--paper); }

  .texture {
    position: absolute;
    top: 0;
    bottom: 0;
  }
  .card--back .texture {
    right: 0;
    width: 58%;
    background: linear-gradient(90deg, rgba(10,10,10,1) 0%, rgba(40,70,15,0.9) 35%, rgba(95,150,40,0.95) 75%, rgba(120,180,50,1) 100%);
  }
  .card--front .texture {
    left: 0;
    width: 55%;
    background: linear-gradient(90deg, rgba(140,198,63,1) 0%, rgba(140,198,63,0.85) 50%, rgba(140,198,63,0.35) 85%, rgba(140,198,63,0) 100%);
  }

  .wordmark {
    position: absolute;
    display: flex;
    align-items: center;
    gap: 12px;
    white-space: nowrap;
    line-height: 1;
  }
  .wordmark__dot {
    border-radius: 50%;
    flex: none;
  }
  .card--back .wordmark {
    left: 62px;
    top: 110px;
    font-size: 42px;
    color: var(--leaf);
  }
  .card--back .wordmark__dot { width: 16px; height: 16px; background: var(--leaf); }
  .card--front .wordmark {
    left: 90px;
    top: 155px;
    font-size: 56px;
    color: var(--leaf-deep);
  }
  .card--front .wordmark__dot { width: 20px; height: 20px; background: var(--leaf-deep); }

  .contact {
    position: absolute;
    left: 62px;
    top: 215px;
    margin: 0;
    padding: 0;
    list-style: none;
    color: var(--text-light);
    font-size: 17px;
    line-height: 26px;
  }
  .contact li {
    display: flex;
    align-items: flex-start;
    gap: 12px;
  }
  .contact svg {
    flex: none;
    width: 14px;
    height: 14px;
    margin-top: 6px;
    fill: var(--leaf);
  }
  .contact .no-icon { padding-left: 26px; }

  .slogan {
    position: absolute;
    right: 44px;
    bottom: 40px;
    margin: 0;
    font-size: 20px;
    color: var(--slogan);
    white-space: nowrap;
  }
</style>
</head>
<body>
<main class="sheet">

  <section class="card card--back" aria-label="Card back">
    <div class="texture" role="img" aria-label="Green grunge paint texture"></div>
    <div class="wordmark"><span class="wordmark__dot"></span>Fernhollow Greens</div>
    <ul class="contact">
      <li>
        <svg viewBox="0 0 14 14" aria-hidden="true"><path d="M7 0a5 5 0 0 0-5 5c0 3.5 5 9 5 9s5-5.5 5-9a5 5 0 0 0-5-5zm0 7a2 2 0 1 1 0-4 2 2 0 0 1 0 4z"/></svg>
        <span>48 Harlow Lane, Brinmoor Bay,<br>VA 23519</span>
      </li>
      <li>
        <svg viewBox="0 0 14 14" aria-hidden="true"><path d="M1 4c0-1.5 2.5-2.5 6-2.5S13 2.5 13 4v1.5h-3V4.2H4v1.3H1z"/><rect x="2.5" y="6.5" width="9" height="6" rx="1"/></svg>
        <span>555-014-2790</span>
      </li>
      <li>
        <svg viewBox="0 0 14 14" aria-hidden="true"><path d="M0 2h14v10H0zM1.2 3.2 7 7.8l5.8-4.6z" fill-rule="evenodd"/></svg>
        <span>hello@fernhollowgreens.com</span>
      </li>
      <li class="no-icon">www.FernhollowGreens.com</li>
    </ul>
  </section>

  <section class="card card--front" aria-label="Card front">
    <div class="texture" role="img" aria-label="Light green grunge paint texture"></div>
    <div class="wordmark"><span class="wordmark__dot"></span>Fernhollow Greens</div>
    <p class="slogan">Fresh as the morning the garden woke up</p>
  </section>

</main>
</body>
</html>
```